Letter head / email signature/ contract document templates

We need a professional email signature and letterhead designed for our established carpentry and maintenance company. Our Logo (attached) was originally designed 6 years ago by design guru and we love it, looking for something to compliment it ( not a home job)

```html
<!DOCTYPE html>
<html lang="en">
<head>
<meta charset="utf-8">
<title>Northgate Fix Maintenance – Letterhead</title>
<link rel="stylesheet" href="https://fonts.googleapis.com/css2?family=Open+Sans:wght@400;700&family=Roboto:wght@400&display=swap">
<style>
  :root {
    --backdrop: #dcdcdc;
    --paper: #f7f7f7;
    --ink: #3a3a3a;
    --ink-soft: #4a4a4a;
    --brand-red: #d91f26;
    --brand-dark: #363636;
    --tool-grey: #9a9a9a;
  }
  * { margin: 0; padding: 0; box-sizing: border-box; }
  html, body {
    width: 1153px; height: 1200px; overflow: hidden;
    background: var(--backdrop);
  }
  .letterhead {
    position: absolute; left: 173px; top: 38px;
    width: 806px; height: 1124px;
    background: var(--paper);
    font-family: "Open Sans", Arial, sans-serif;
    color: var(--ink-soft);
  }
  .brand {
    position: absolute; left: 78px; top: 112px;
    display: flex; align-items: center; gap: 8px;
    font-family: "Open Sans", Arial, sans-serif;
    font-weight: 700; font-size: 19px; line-height: 24px;
    color: var(--brand-dark);
  }
  .brand-mark { width: 14px; height: 14px; background: var(--brand-red); flex: none; }
  .contact {
    position: absolute; left: 558px; top: 82px;
    font-family: "Roboto", Arial, sans-serif; font-size: 12.4px;
    line-height: 16px; color: var(--ink);
    list-style: none;
  }
  .contact li { display: flex; align-items: center; gap: 4px; white-space: nowrap; }
  .contact .address-line:nth-child(2) { margin-bottom: 2px; }
  .contact svg { width: 11px; height: 11px; fill: var(--brand-red); flex: none; }
  .letter-body {
    position: absolute; left: 72px; top: 264px; width: 661px;
    font-size: 14.6px; line-height: 21.7px;
  }
  .letter-body p { margin-bottom: 21.7px; text-align: justify; }
  .letter-body .salutation, .letter-body .closing { text-align: left; }
  .signature {
    position: absolute; left: 72px; top: 836px; width: 96px; height: 90px;
    background: linear-gradient(135deg, #ececec, #e2e2e2);
  }
  .footer-band { position: absolute; top: 1064px; height: 21px; }
  .footer-band.dark { left: 107px; width: 133px; background: var(--brand-dark); }
  .footer-band.red { left: 245px; width: 418px; background: var(--brand-red); }
  .tool-art { position: absolute; }
  .tool-art.wrench { left: 72px; top: 1055px; width: 35px; height: 39px; background: var(--brand-dark); }
  .tool-art.roller { left: 663px; top: 1045px; width: 69px; height: 58px; background: linear-gradient(90deg, #8c8c8c, #b4b4b4); }
</style>
</head>
<body>
<main class="letterhead">
  <header>
    <div class="brand"><span class="brand-mark"></span>Northgate Fix Maintenance</div>
    <ul class="contact">
      <li class="address-line">48 Cedar Ridge Lane,</li>
      <li class="address-line">Oakview, ON L2K 4P7</li>
      <li><svg viewBox="0 0 12 12"><path d="M1 4c2-3 8-3 10 0l-2 1.5-1-1.5H4L3 5.5zM3 6h6l1 5H2z"/></svg>905.555.0142</li>
      <li><svg viewBox="0 0 12 12"><path d="M1 3h10v6H1z M1 3l5 4 5-4" stroke="#f7f7f7" stroke-width="0.8"/></svg>info@northgatefix.com</li>
      <li><svg viewBox="0 0 12 12"><circle cx="6" cy="6" r="5"/><path d="M4 3c1 1 0 2 1 3s2 0 2 2" stroke="#f7f7f7" stroke-width="1" fill="none"/></svg>www.northgatefix.com</li>
    </ul>
  </header>

  <section class="letter-body">
    <p class="salutation">Dear customer,</p>
    <p>Lorem ipsum dolor sit amet, consectetur adipisicing elit, sed do eiusmod tempor incididunt ut labore et dolore magna aliqua. Ut enim ad minim veniam, quis nostrud exercitation ullamco laboris nisi ut aliquip ex ea commodo consequat. Duis aute irure dolor in reprehenderit in voluptate velit esse cillum dolore eu fugiat nulla pariatur. Excepteur sint occaecat cupidatat non proident, sunt in culpa qui officia deserunt mollit anim id est laborum.</p>
    <p>Lorem ipsum dolor sit amet, consectetur adipisicing elit, sed do eiusmod tempor incididunt ut labore et dolore magna aliqua. Ut enim ad minim veniam, quis nostrud exercitation ullamco laboris nisi ut aliquip ex ea commodo consequat. Duis aute irure dolor in reprehenderit in voluptate velit esse cillum dolore eu fugiat nulla pariatur. Excepteur sint occaecat cupidatat non proident, sunt in culpa qui officia deserunt mollit anim id est laborum.</p>
    <p>Lorem ipsum dolor sit amet, consectetur adipisicing elit, sed do eiusmod tempor incididunt ut labore et dolore magna aliqua. Ut enim ad minim veniam, quis nostrud exercitation ullamco laboris nisi ut aliquip ex ea commodo consequat. Duis aute irure dolor in reprehenderit in voluptate velit esse cillum dolore eu fugiat nulla pariatur. Excepteur sint occaecat cupidatat non proident, sunt in culpa qui officia deserunt mollit anim id est laborum.</p>
    <p>Lorem ipsum dolor sit amet, consectetur adipisicing elit, sed do eiusmod tempor incididunt ut labore et dolore magna aliqua. Ut enim ad minim veniam, quis nostrud exercitation ullamco laboris nisi ut aliquip ex ea commodo consequat. Duis aute irure dolor in reprehenderit.</p>
    <p class="closing">Yours Sincerely,</p>
  </section>

  <div class="signature" role="img" aria-label="Handwritten signature"></div>

  <footer>
    <div class="tool-art wrench" role="img" aria-label="Wrench illustration"></div>
    <div class="footer-band dark"></div>
    <div class="footer-band red"></div>
    <div class="tool-art roller" role="img" aria-label="Paint roller illustration"></div>
  </footer>
</main>
</body>
</html>
```